Pheasant Farm needs a logo design

I need a logo design for my Pheasant farm. We raise Pheasants from chicks to adult birds for the hunting clubs dog training and restocking. I would like a logo that makes it easy to see that we deal with Pheasants. My company name is Larkin Meadow Pines located in northern MN. I'd like a pheasant in the logo if possible.

Target Market(s)

Hunting clubs, dog trainers, hunters

Contact Information for Business Card

Larkin Meadow Pines Dale Wexby cell 715-463-2098 office 218-302-7746 tallgrassfowlyard.com tallgrassfowlyard@quailpostmail.com
5816 Bramwell Rd NE
Corvale Springs, ND 56519

```html
<!DOCTYPE html>
<html lang="en">
<head>
<meta charset="utf-8">
<title>Larkin Meadow Pines – Business Card</title>
<link rel="stylesheet" href="https://fonts.googleapis.com/css2?family=Arimo:wght@400;700&family=Open+Sans:wght@400;600&display=swap">
<style>
  :root {
    --backdrop: #1c1c1c;
    --brand-orange: #e85620;
    --card-white: #ffffff;
    --text-grey: #6f6f6f;
    --divider: #dcdcdc;
  }
  * { margin: 0; padding: 0; box-sizing: border-box; }
  html, body { width: 1200px; height: 900px; overflow: hidden; }
  body {
    background: var(--backdrop);
    font-family: "Arimo", Arial, sans-serif;
    position: relative;
  }
  .card {
    position: absolute;
    left: 300px;
    width: 600px;
    height: 343px;
    box-shadow: 0 10px 30px rgba(0,0,0,0.45);
  }
  .card-front {
    top: 80px;
    background: var(--brand-orange);
    color: var(--card-white);
  }
  .front-name {
    position: absolute;
    left: 0; right: 0; top: 130px;
    text-align: center;
    font-family: "Open Sans", Arial, sans-serif;
    font-weight: 600;
    font-size: 34px;
    letter-spacing: 0.5px;
  }
  .front-url {
    position: absolute;
    left: 0; right: 0; bottom: 34px;
    text-align: center;
    font-family: "Open Sans", Arial, sans-serif;
    font-size: 14px;
  }
  .card-back {
    top: 477px;
    background: var(--card-white);
  }
  .back-brand {
    position: absolute;
    left: 34px; top: 150px;
    display: flex;
    align-items: center;
    gap: 10px;
  }
  .brand-square {
    width: 22px; height: 22px;
    background: var(--brand-orange);
  }
  .brand-name {
    font-weight: 700;
    font-size: 21px;
    color: var(--brand-orange);
  }
  .divider {
    position: absolute;
    left: 290px; top: 40px;
    width: 1px; height: 250px;
    background: var(--divider);
  }
  .contact {
    position: absolute;
    left: 312px; top: 56px;
    color: var(--text-grey);
    font-size: 14px;
  }
  .contact-name {
    color: var(--brand-orange);
    font-weight: 700;
    font-size: 19px;
    text-transform: uppercase;
    margin-bottom: 8px;
  }
  .contact-line {
    display: flex;
    align-items: center;
    gap: 8px;
    line-height: 19px;
  }
  .contact-line svg { width: 12px; height: 12px; flex: none; }
  .web-domain { color: var(--brand-orange); }
  .address {
    margin-top: 14px;
    font-size: 15px;
    line-height: 19px;
  }
</style>
</head>
<body>
  <section class="card card-front">
    <div class="front-name">Larkin Meadow Pines</div>
    <div class="front-url">www.tallgrassfowlyard.com</div>
  </section>

  <section class="card card-back">
    <div class="back-brand">
      <span class="brand-square"></span>
      <span class="brand-name">Larkin Meadow Pines</span>
    </div>
    <div class="divider"></div>
    <div class="contact">
      <div class="contact-name">Dale Wexby</div>
      <div class="contact-line">
        <svg viewBox="0 0 12 12"><path d="M1 4 Q6 0 11 4 L10 6 L8 5 L8 4 Q6 3 4 4 L4 5 L2 6 Z M3 7 H9 L10 11 H2 Z" fill="var(--brand-orange)"/></svg>
        <span>218-302-7746</span>
      </div>
      <div class="contact-line">
        <svg viewBox="0 0 12 12"><rect x="3" y="0.5" width="6" height="11" rx="1.2" fill="none" stroke="var(--brand-orange)" stroke-width="1.2"/><circle cx="6" cy="9.5" r="0.7" fill="var(--brand-orange)"/></svg>
        <span>715-463-2098</span>
      </div>
      <div class="contact-line">
        <svg viewBox="0 0 12 12"><rect x="0.5" y="2" width="11" height="8" fill="var(--brand-orange)"/><path d="M0.5 2 L6 7 L11.5 2" fill="none" stroke="#fff" stroke-width="1"/></svg>
        <span>tallgrassfowlyard@quailpostmail.com</span>
      </div>
      <div class="contact-line">
        <svg viewBox="0 0 12 12"><circle cx="6" cy="6" r="5.5" fill="var(--brand-orange)"/><path d="M0.5 6 H11.5 M6 0.5 Q3 6 6 11.5 M6 0.5 Q9 6 6 11.5" fill="none" stroke="#fff" stroke-width="0.8"/></svg>
        <span>www.<span class="web-domain">tallgrassfowlyard</span>.com</span>
      </div>
      <div class="address">
        5816 Bramwell Rd NE<br>
        Corvale Springs, ND 56519
      </div>
    </div>
  </section>
</body>
</html>
```